Brochure for a paper wholesaler who wants to educate his print industry clients

We will be making a stapled informative brochure, that contains basic information about our paper products - the types of paper there is, their characteristics and other useful information.
As we are part of a paper wholesaler group in Europe - ORVANTE, we received a brochure in German that has this kind of information. The text in it is not as important. What is important is the layout of the document and how the text will appear in it (added in the uploaded files - 210915_Wiessenswertes_TKLM_F51.pdf).
We are allowed to tinker with this file and adjust it to our needs. So there are also .idml and .indd files available (also in the uploaded files).
We would like to keep the custom page size of 210 x290mm (8.3x11.4 in), or you can go up to 210x297mm (8.3x11.7 in).
What we want is a modern looking design that contains our companies red bordo and white/ grey colours to replace the existing green colours in this borchure. The pictures and appearance of the file can be changed according to your views and what you think would look good. We don't necessarily want to keep the same design, we just want the layout of the document be the same, as we will be placing our translated text into it. The ORVANTE logo should be replaced with our own logo (KEMSU Logo.png).
As for how it could look, it could go together with our paper presentation, for which the design can be seen in the "KEMSU Base - v2.pptx".
Holiday season, so have a lot of tasks to take care of and not as much time to check PixelForge as often.

```html
<!DOCTYPE html>
<html lang="de">
<head>
<meta charset="utf-8">
<title>KEMSU – Wissenswert! Broschüre</title>
<link href="https://fonts.googleapis.com/css2?family=Manrope:wght@300;400;500;600;700&family=Inter:wght@300;400&display=swap" rel="stylesheet">
<style>
  :root {
    --board: #b29a7b;
    --paper: #ffffff;
    --bordo: #862e34;
    --grey: #aeb3c2;
    --ink: #2b2b2b;
    --soft: #e9eaec;
    --rule: #c9ccd3;
  }
  * { margin: 0; padding: 0; box-sizing: border-box; }
  html, body { width: 848px; height: 1200px; overflow: hidden; background: var(--board); }
  .board { position: relative; width: 848px; height: 1200px; font-family: "Manrope", sans-serif; }
  .label {
    position: absolute; width: 200px; margin-left: -100px; text-align: center;
    font-family: "Inter", sans-serif; font-weight: 300; color: #fff; font-size: 12px;
  }
  .label::after {
    content: ""; display: block; width: 1px; height: 8px; margin: 5px auto 0; background: #fff;
  }
  .spread { position: absolute; left: 124px; width: 600px; height: 424px; display: flex; }
  .spread--top { top: 120px; }
  .spread--inner { top: 657px; }
  .page { width: 300px; height: 424px; background: var(--paper); }
  .page + .page { border-left: 1px solid #ececec; }
  .page svg { display: block; width: 100%; height: 100%; }
  .note {
    position: absolute; left: 0; right: 0; top: 1171px; text-align: center;
    font-family: "Inter", sans-serif; font-weight: 300; color: #fff; font-size: 11.5px;
  }
  .ct { font-size: 8.3px; fill: var(--ink); font-weight: 400; }
  .ct .firm { fill: var(--bordo); font-weight: 700; }
  .brand { fill: var(--bordo); font-weight: 500; letter-spacing: 0.55em; }
  .cover-title { fill: var(--bordo); font-size: 22px; font-weight: 400; }
  .cover-sub { fill: var(--ink); font-size: 16px; font-weight: 300; }
  .cover-note { fill: var(--ink); font-size: 7.5px; }
  .cover-side { fill: var(--ink); font-size: 12px; font-weight: 400; }
  .h-contents { fill: var(--ink); font-size: 32px; font-weight: 600; }
  .toc { fill: var(--ink); font-size: 10.5px; font-weight: 300; }
  .h-section { fill: var(--bordo); font-size: 20px; font-weight: 600; }
  .h-sub { fill: var(--ink); font-size: 10px; font-weight: 700; }
  .h-sub-red { fill: var(--bordo); font-size: 11.5px; font-weight: 600; }
  .term { fill: var(--ink); font-size: 10px; font-weight: 700; }
  .def { fill: var(--ink); font-size: 10px; font-weight: 300; }
  .abbr { fill: var(--ink); font-size: 10px; font-weight: 700; }
  .abbr-en, .abbr-de { fill: var(--ink); font-size: 10px; font-weight: 300; }
  .foot-brand { fill: var(--bordo); font-size: 13px; font-weight: 600; letter-spacing: 0.1em; }
</style>
</head>
<body>
<main class="board">

  <p class="label" style="left:273px;top:68px;">Last Page</p>
  <p class="label" style="left:573px;top:68px;">Front Page</p>

  <section class="spread spread--top">
    <!-- Back cover: dealer directory -->
    <article class="page page--back">
      <svg viewBox="0 0 573 810">
        <g class="partner-badges" fill="#c4c4c4">
          <rect x="52" y="44" width="16" height="16"/>
          <rect x="172" y="42" width="16" height="18"/>
          <circle cx="311" cy="59" r="8"/>
          <circle cx="449" cy="59" r="8"/>
          <rect x="50" y="323" width="32" height="10" rx="2"/>
          <rect x="170" y="321" width="14" height="14"/>
          <rect x="441" y="218" width="16" height="14"/>
        </g>

        <g class="dealer-marks" stroke="var(--bordo)" stroke-width="2">
          <line x1="43" y1="71" x2="43" y2="81"/><line x1="43" y1="152" x2="43" y2="162"/>
          <line x1="43" y1="232" x2="43" y2="242"/><line x1="43" y1="339" x2="43" y2="349"/>
          <line x1="43" y1="408" x2="43" y2="418"/>
          <line x1="163" y1="71" x2="163" y2="81"/><line x1="163" y1="152" x2="163" y2="162"/>
          <line x1="163" y1="232" x2="163" y2="242"/><line x1="163" y1="339" x2="163" y2="349"/>
          <line x1="163" y1="408" x2="163" y2="418"/>
          <line x1="296" y1="71" x2="296" y2="81"/><line x1="296" y1="152" x2="296" y2="162"/>
          <line x1="296" y1="232" x2="296" y2="242"/><line x1="296" y1="313" x2="296" y2="323"/>
          <line x1="296" y1="382" x2="296" y2="392"/>
          <line x1="434" y1="71" x2="434" y2="81"/><line x1="434" y1="152" x2="434" y2="162"/>
          <line x1="434" y1="235" x2="434" y2="245"/>
        </g>

        <g class="dealer-list">
          <text class="ct" x="50" y="80"><tspan class="firm">HALDEN &amp; CO.</tspan><tspan x="50" dy="11.5">(GmbH &amp; Co.) KG</tspan><tspan x="50" dy="11.5">Brückenweg 12</tspan><tspan x="50" dy="11.5">21480 Lindhof</tspan><tspan x="50" dy="11.5">T +49 (0)40 5 31 48-0</tspan><tspan x="50" dy="11.5">F +49 (0)40 5 31 48-466</tspan></text>
          <text class="ct" x="50" y="161"><tspan class="firm">HALDEN &amp; CO.</tspan><tspan x="50" dy="11.5">(GmbH &amp; Co.) KG</tspan><tspan x="50" dy="11.5">Lindenallee 24</tspan><tspan x="50" dy="11.5">12470 Berlin</tspan><tspan x="50" dy="11.5">T +49 (0)30 4 62 18-0</tspan><tspan x="50" dy="11.5">F +49 (0)30 4 62 18-444</tspan></text>
          <text class="ct" x="50" y="241"><tspan class="firm">HALDEN &amp; CO.</tspan><tspan x="50" dy="11.5">(GmbH &amp; Co.) KG</tspan><tspan x="50" dy="11.5">Hafenkamp 8</tspan><tspan x="50" dy="11.5">24150 Kiel</tspan><tspan x="50" dy="11.5">T +49 (0)40 5 31 48-0</tspan><tspan x="50" dy="11.5">F +49 (0)40 5 31 48-466</tspan></text>
          <text class="ct" x="50" y="348"><tspan class="firm">pvk</tspan> GmbH &amp; Co. KG<tspan x="50" dy="11.5">Mühlenstraße 6</tspan><tspan x="50" dy="11.5">30970 Kornhagen</tspan><tspan x="50" dy="11.5">T +49 (0)5 11 37 62-0</tspan><tspan x="50" dy="11.5">F +49 (0)5 11 37 62-290</tspan></text>
          <text class="ct" x="50" y="417"><tspan class="firm">pvk</tspan> GmbH &amp; Co. KG<tspan x="50" dy="11.5">Weidenstraße 118</tspan><tspan x="50" dy="11.5">33610 Bielefeld</tspan><tspan x="50" dy="11.5">T +49 (0)5 21 48 31-0</tspan><tspan x="50" dy="11.5">F +49 (0)5 21 4 83 17 22</tspan></text>

          <text class="ct" x="170" y="80"><tspan class="firm">BRANDT &amp; LOEWE</tspan><tspan x="170" dy="11.5">GmbH &amp; Co. KG</tspan><tspan x="170" dy="11.5">Ahornweg 190–204</tspan><tspan x="170" dy="11.5">50760 Köln</tspan><tspan x="170" dy="11.5">T +49 (0)2 21 58 30-0</tspan><tspan x="170" dy="11.5">F +49 (0)2 21 58 30-500</tspan></text>
          <text class="ct" x="170" y="161"><tspan class="firm">BRANDT &amp; LOEWE</tspan><tspan x="170" dy="11.5">GmbH &amp; Co. KG</tspan><tspan x="170" dy="11.5">Kanalufer 37</tspan><tspan x="170" dy="11.5">44150 Dortmund</tspan><tspan x="170" dy="11.5">T +49 (0)2 31 64 72-0</tspan><tspan x="170" dy="11.5">F +49 (0)2 31 64 72-100</tspan></text>
          <text class="ct" x="170" y="241"><tspan class="firm">BRANDT &amp; LOEWE</tspan><tspan x="170" dy="11.5">GmbH &amp; Co. KG</tspan><tspan x="170" dy="11.5">Gewerbepark Talheim</tspan><tspan x="170" dy="11.5">Im Wiesengrund</tspan><tspan x="170" dy="11.5">54320 Moselbach</tspan><tspan x="170" dy="11.5">T +49 (0)6 51 7 42 19-0</tspan><tspan x="170" dy="11.5">F +49 (0)6 51 7 42 19-10</tspan></text>
          <text class="ct" x="170" y="348"><tspan class="firm">3K</tspan> GmbH &amp; Co. KG<tspan x="170" dy="11.5">Werkstraße 41</tspan><tspan x="170" dy="11.5">85760 Eichenried bei München</tspan><tspan x="170" dy="11.5">T +49 (0)89 6 27 40-0</tspan><tspan x="170" dy="11.5">F +49 (0)89 6 27 40-100</tspan></text>
          <text class="ct" x="170" y="417"><tspan class="firm">3K</tspan> GmbH &amp; Co. KG<tspan x="170" dy="11.5">Flussgasse 16</tspan><tspan x="170" dy="11.5">90460 Nürnberg</tspan><tspan x="170" dy="11.5">T +49 (0)9 11 73 58-0</tspan><tspan x="170" dy="11.5">F +49 (0)9 11 73 58-222</tspan></text>

          <text class="ct" x="303" y="80"><tspan class="firm">ORVANTE GROSSHANDEL</tspan> GmbH<tspan x="303" dy="11.5">Handelsring 3</tspan><tspan x="303" dy="11.5">06120 Feldau</tspan><tspan x="303" dy="11.5">T +49 (0)3 45 81 37-600</tspan><tspan x="303" dy="11.5">F +49 (0)3 45 81 37-899</tspan></text>
          <text class="ct" x="303" y="161"><tspan class="firm">ORVANTE GROSSHANDEL</tspan> GmbH<tspan x="303" dy="11.5">Fabrikstraße 5</tspan><tspan x="303" dy="11.5">64820 Altheim</tspan><tspan x="303" dy="11.5">T +49 (0)60 52 74 19-0</tspan><tspan x="303" dy="11.5">F +49 (0)60 52 74 19-100</tspan></text>
          <text class="ct" x="303" y="241"><tspan class="firm">ORVANTE GROSSHANDEL</tspan> GmbH<tspan x="303" dy="11.5">Am Birkenhang 4</tspan><tspan x="303" dy="11.5">99880 Steinbrück/</tspan><tspan x="303" dy="11.5">OT Wiesen</tspan><tspan x="303" dy="11.5">T +49 (0)36 41 58 27-0</tspan><tspan x="303" dy="11.5">F +49 (0)36 41 58 27-20</tspan></text>
          <text class="ct" x="303" y="322"><tspan class="firm">ORVANTE GROSSHANDEL</tspan> GmbH<tspan x="303" dy="11.5">Seeweg 9</tspan><tspan x="303" dy="11.5">17230 Marlow</tspan><tspan x="303" dy="11.5">T +49 (0)3 99 46 13 07-0</tspan><tspan x="303" dy="11.5">F +49 (0)3 99 46 13 07-90</tspan></text>
          <text class="ct" x="303" y="391"><tspan class="firm">ORVANTE GROSSHANDEL</tspan> GmbH<tspan x="303" dy="11.5">Bergstraße 31</tspan><tspan x="303" dy="11.5">01460 Talhausen</tspan><tspan x="303" dy="11.5">T +49 (0)3 52 47 16 2-0</tspan><tspan x="303" dy="11.5">F +49 (0)3 52 47 16 2-55</tspan></text>

          <text class="ct" x="441" y="80"><tspan class="firm">WERNAU</tspan> GmbH &amp; Co. KG<tspan x="441" dy="11.5">Hauptstraße 61</tspan><tspan x="441" dy="11.5">73440 Ostheim/Württemberg</tspan><tspan x="441" dy="11.5">T +49 (0)73 42 18 6-0</tspan><tspan x="441" dy="11.5">F +49 (0)73 42 18 6-170</tspan></text>
          <text class="ct" x="441" y="161"><tspan class="firm">WERNAU</tspan> GmbH &amp; Co. KG<tspan x="441" dy="11.5">Am Erlenbach 3</tspan><tspan x="441" dy="11.5">77890 Rheintal</tspan><tspan x="441" dy="11.5">T +49 (0)78 52 63 40-0</tspan><tspan x="441" dy="11.5">F +49 (0)78 52 63 40-344</tspan></text>
          <text class="ct" x="441" y="244"><tspan class="firm">NORDLAND GmbH &amp; Co. KG</tspan><tspan x="441" dy="11.5">Großhandel</tspan><tspan x="441" dy="11.5">Deichstraße 15</tspan><tspan x="441" dy="11.5">28310 Bremen</tspan><tspan x="441" dy="11.5">T +49 (0)4 21 63 85 7-0</tspan><tspan x="441" dy="11.5">F +49 (0)4 21 63 85 7-200</tspan></text>
        </g>

        <g class="back-geometry">
          <polygon points="573,468 573,506 348,704 338,676" fill="var(--grey)"/>
          <polygon points="573,523 573,759 338,759" fill="var(--bordo)"/>
          <polygon points="0,759 336,759 322,773 0,773" fill="var(--bordo)"/>
          <polygon points="324,775 573,775 573,810 285,810" fill="var(--bordo)"/>
        </g>

        <text class="brand" x="111" y="736" text-anchor="middle" font-size="22">KEMSU</text>
      </svg>
    </article>

    <!-- Front cover -->
    <article class="page page--front">
      <svg viewBox="0 0 573 810">
        <path d="M193,143 H56 V750 H514 V143 H377" fill="none" stroke="var(--grey)" stroke-width="9"/>
        <text class="brand" x="290" y="153" text-anchor="middle" font-size="22">KEMSU</text>
        <text class="cover-title" x="80" y="196">Wissenswert!</text>
        <text class="cover-sub" x="80" y="218">Formate, Klassen, Farben, Berechnungen</text>
        <text class="cover-note" x="80" y="232">Wegweiser für den Umgang mit Papier und Karton</text>

        <polygon points="254,351 330,502 178,502" fill="var(--grey)"/>
        <polygon points="305,251 557,754 522,754 285,292" fill="var(--bordo)"/>

        <defs>
          <linearGradient id="pagesTone" x1="0" y1="0" x2="1" y2="1">
            <stop offset="0" stop-color="#f4f4f4"/>
            <stop offset="0.6" stop-color="#dcdcdc"/>
            <stop offset="1" stop-color="#f7f7f7"/>
          </linearGradient>
        </defs>
        <polygon role="img" aria-label="Foto: aufgefächerte weiße Papierseiten eines offenen Buches"
                 points="201,538 405,538 479,719 109,719" fill="url(#pagesTone)" stroke="var(--bordo)" stroke-width="1"/>
        <text class="cover-side" transform="translate(99,702) rotate(-63)">Die kleine Papier- und Farbfibel</text>
      </svg>
    </article>
  </section>

  <p class="label" style="left:273px;top:601px;">Inner</p>
  <p class="label" style="left:573px;top:601px;">Inner</p>

  <section class="spread spread--inner">
    <!-- Contents page -->
    <article class="page page--contents">
      <svg viewBox="0 0 573 810">
        <polygon points="0,80 55,53 55,76 0,102" fill="var(--bordo)"/>
        <text class="h-contents" x="63" y="77">Inhalt</text>
        <line x1="155" y1="76" x2="508" y2="76" stroke="var(--rule)" stroke-width="1"/>

        <g class="toc">
          <text x="65" y="117">Fachlatein für Fortgeschrittene</text><text x="509" y="117" text-anchor="end">03</text>
          <text x="65" y="137">Karton im Überblick</text><text x="509" y="137" text-anchor="end">04</text>
          <text x="65" y="157">Das kleine 1x1 der Formatschule</text><text x="509" y="157" text-anchor="end">04</text>
          <text x="65" y="177">Umfangreiche Sache</text><text x="509" y="177" text-anchor="end">05</text>
          <text x="65" y="197">Hilfe bei Gewichtsproblemen</text><text x="509" y="197" text-anchor="end">06</text>
          <text x="65" y="217">Die feine Art zu drucken</text><text x="509" y="217" text-anchor="end">07</text>
          <text x="65" y="237">Wegweiser für die Laufrichtung</text><text x="509" y="237" text-anchor="end">08</text>
          <text x="65" y="257">Garantierte Farben</text><text x="509" y="257" text-anchor="end">10</text>
          <text x="65" y="277">Natürlich der Umwelt zuliebe</text><text x="509" y="277" text-anchor="end">10</text>
        </g>

        <defs>
          <linearGradient id="coralTone" x1="0" y1="0" x2="0" y2="1">
            <stop offset="0" stop-color="#f6a196"/>
            <stop offset="0.55" stop-color="#f0857a"/>
            <stop offset="1" stop-color="#d96a5f"/>
          </linearGradient>
        </defs>
        <polygon points="41,431 237,380 237,401 41,453" fill="var(--grey)"/>
        <polygon role="img" aria-label="Foto: offenes Buch mit herzförmig gefalteten Seiten auf korallrotem Grund"
                 points="41,471 533,346 533,578 41,705" fill="url(#coralTone)"/>
        <polygon points="533,578 533,605 440,629 440,602" fill="var(--grey)"/>
        <polygon points="41,700 338,624 338,660 41,736" fill="var(--bordo)" opacity="0.85"/>
        <line x1="41" y1="722" x2="446" y2="620" stroke="var(--bordo)" stroke-width="1.2"/>
        <polygon points="41,738 237,688 237,713 41,763" fill="var(--bordo)"/>

        <line x1="41" y1="780" x2="475" y2="780" stroke="var(--bordo)" stroke-width="3"/>
        <text class="foot-brand" x="532" y="784" text-anchor="end">KEMSU</text>
      </svg>
    </article>

    <!-- Glossary page -->
    <article class="page page--glossary">
      <svg viewBox="0 0 573 810">
        <line x1="0" y1="80" x2="26" y2="66" stroke="var(--grey)" stroke-width="4"/>
        <text class="h-section" x="32" y="77">Fachlatein für Fortgeschrittene</text>
        <line x1="350" y1="76" x2="541" y2="76" stroke="var(--rule)" stroke-width="1"/>
        <text class="h-sub" x="32" y="108">Die gebräuchlichsten Fachbegriffe und Abkürzungen</text>

        <g class="glossary-rules" stroke="var(--rule)" stroke-width="1">
          <line x1="32" y1="153" x2="541" y2="153"/><line x1="32" y1="189" x2="541" y2="189"/>
          <line x1="32" y1="240" x2="541" y2="240"/><line x1="32" y1="278" x2="541" y2="278"/>
          <line x1="32" y1="316" x2="541" y2="316"/><line x1="32" y1="353" x2="541" y2="353"/>
        </g>

        <text class="term" x="32" y="130">ungestrichen</text>
        <text class="def" x="164" y="130">Unveredelte, maschinenglatte oder satinierte Papiere, die aus<tspan x="164" dy="15">verschiedenen Faserstoffen hergestellt werden können.</tspan></text>
        <text class="term" x="32" y="168">satiniert/<tspan x="32" dy="15">scharf satiniert</tspan></text>
        <text class="def" x="164" y="168">In einem Kalander nachträglich und unterschiedlich stark geglättete Papiere.</text>
        <text class="term" x="32" y="203">gestrichen</text>
        <text class="def" x="164" y="203">Die Oberfläche des Papiers wird bereits in der Papiermaschine oder<tspan x="164" dy="15">nachträglich in einer Streichmaschine durch einen Strichauftrag veredelt.</tspan><tspan x="164" dy="15">Daraus ergibt sich eine bessere Druckwiedergabe.</tspan></text>
        <text class="term" x="32" y="255">matt gestrichen</text>
        <text class="def" x="164" y="255">Die Oberfläche des Papiers wird in einem zusätzlichen Arbeitsgang mit<tspan x="164" dy="15">matten Pigmenten gestrichen.</tspan></text>
        <text class="term" x="32" y="293">halbmatt gestrichen/<tspan x="32" dy="15">gestrichen (silk/satin)</tspan></text>
        <text class="def" x="164" y="293">Ein besonderer Strichauftrag und/oder spezielles Kalandrieren erzeugen<tspan x="164" dy="15">eine halbmatte Oberfläche.</tspan></text>
        <text class="term" x="32" y="331">glänzend gestrichen</text>
        <text class="def" x="164" y="331">Durch nachträgliches Satinieren und einen speziellen Strichauftrag<tspan x="164" dy="15">entsteht eine glänzende Oberfläche.</tspan></text>
        <text class="term" x="32" y="368">FCO</text>
        <text class="def" x="164" y="368">In der Papiermaschine (inline) gestrichenes Papier mit matter oder<tspan x="164" dy="15">glänzender Oberfläche.</tspan></text>

        <line x1="0" y1="470" x2="26" y2="456" stroke="var(--grey)" stroke-width="4"/>
        <text class="h-sub-red" x="32" y="459">Abkürzungen und ihre Übersetzung</text>
        <line x1="244" y1="457" x2="541" y2="457" stroke="var(--rule)" stroke-width="1"/>

        <rect x="33" y="474" width="507" height="235" fill="var(--soft)"/>
        <g class="abbr-table">
          <text class="abbr" x="40" y="491">WFU</text><text class="abbr-en" x="118" y="491">woodfree, uncoated</text><text class="abbr-de" x="286" y="491">holzfrei ungestrichen</text>
          <text class="abbr" x="40" y="508">MFS</text><text class="abbr-en" x="118" y="508">machine-finished special</text><text class="abbr-de" x="286" y="508">holzhaltig, maschinenglatt, ungestrichen</text>
          <text class="abbr" x="40" y="525">WFC</text><text class="abbr-en" x="118" y="525">woodfree, coated</text><text class="abbr-de" x="286" y="525">holzfrei gestrichen</text>
          <text class="abbr" x="40" y="543">MWC</text><text class="abbr-en" x="118" y="543">middleweight, coated</text><text class="abbr-de" x="286" y="543">doppelt gestrichen, holzhaltig, hoher Weißegrad,<tspan x="286" dy="17">mittleres Gewicht</tspan></text>
          <text class="abbr" x="40" y="578">LWC</text><text class="abbr-en" x="118" y="578">lightweight, coated</text><text class="abbr-de" x="286" y="578">einfach gestrichen, holzhaltig</text>
          <text class="abbr" x="40" y="595">ULWC</text><text class="abbr-en" x="118" y="595">ultralightweight, coated</text><text class="abbr-de" x="286" y="595">einfach gestrichen, holzhaltig, ultraleichtgewichtig</text>
          <text class="abbr" x="40" y="612">MFC</text><text class="abbr-en" x="118" y="612">machine-finished, coated</text><text class="abbr-de" x="286" y="612">maschinenglatt gestrichen, holzhaltig</text>
          <text class="abbr" x="40" y="630">SC-A PLUS</text><text class="abbr-en" x="118" y="630">supercalendered, bright/white</text><text class="abbr-de" x="286" y="630">superkalandriert, holzhaltig, hoher Weißegrad</text>
          <text class="abbr" x="40" y="647">SC-A</text><text class="abbr-en" x="118" y="647">supercalendered</text><text class="abbr-de" x="286" y="647">superkalandriert, holzhaltig, Standard</text>
          <text class="abbr" x="40" y="664">SC-B</text><text class="abbr-en" x="118" y="664">softcalendered</text><text class="abbr-de" x="286" y="664">softkalandriert, holzhaltig</text>
          <text class="abbr" x="40" y="681">FCO</text><text class="abbr-en" x="118" y="681">film coated offset</text><text class="abbr-de" x="286" y="681">in der Papiermaschine (inline) gestrichenes Papier</text>
          <text class="abbr" x="40" y="699">HSWO</text><text class="abbr-en" x="118" y="699">heatset web offset</text><text class="abbr-de" x="286" y="699">Rollenoffset mit Heißlufttrocknung</text>
        </g>

        <line x1="33" y1="780" x2="483" y2="780" stroke="var(--bordo)" stroke-width="3"/>
        <text class="foot-brand" x="540" y="784" text-anchor="end">KEMSU</text>
      </svg>
    </article>
  </section>

  <p class="note">Note. Once You Decide On The Theme, We Will Do More Pages Later.</p>
</main>
</body>
</html>
```